Premium CBD/Hemp company needs packaging and label design

Verdant Halcyon Labs, a premium CBD/Hemp company based in Scottsdale, Arizona is in need of a packaging and label design. We are launching with our flagship product which will be a 30 count capsule and will come in three functions: Pain Relief, Anxiety Support, and Sleep Support. For the purpose of this contest, please design packaging and label for our Anxiety Support product. Our products are physician formulated and all natural. Our main ingredient is CBD/Hemp and is complemented by specific herbs that synergistically work together to give the customer the most effective and desired result. We would like our branding to have a pharmaceutical look and feel with a focus on trust and transparency. We have uploaded our company logo that is to be used on both the packaging and label. We have also uploaded an executed branding questionnaire that will guide you to exactly what we are seeking to achieve as to the look and feel of our brand. Please feel free to contact us with any questions that you may have. The winner of this contest will have the opportunity to work with us on future projects as we will need packaging and label design for our entire Verdant Halcyon Labs product line.

Target Market(s)

See attached branding questionnaire

Industry/Entity Type

Health And Wellness

Font styles to use
Sans Serif

Colors

Designer to choose colors to be used in the design.

Requirements
Must have
• See attached branding questionnaire; Please superimpose labels onto a cobalt blue capsule bottle (see attached)
• >>UPON REVIEW of the FIRST 8 designs, we really like the silver, mildly metallic label background in DESIGN # 21300528, we do not want metalic lettering as that would not look very "Pharmaceutical"
• >>We are in search of a look that is a bit more "Pharmaceutical" than a look that would be more commonly found in a Supplement Store
Nice to have
• "See attached branding questionnaire
Should not have
• See attached branding questionnaire; NO marijuana or cannabis plant on the packaging or label

```html
<!DOCTYPE html>
<html lang="en">
<head>
<meta charset="utf-8">
<title>Verdant Halcyon Labs – Anxiety Relief Label</title>
<link rel="stylesheet" href="https://fonts.googleapis.com/css2?family=Open+Sans:wght@400;600&family=Roboto+Condensed:wght@700&display=swap">
<style>
  :root {
    --page-bg: #ffffff;
    --label-black: #050708;
    --circle-dark: #0d1416;
    --circle-edge: #1f5a60;
    --brand-blue: #4a4fb2;
    --teal-text: #2c8c96;
    --band-light: #2e7f8a;
    --band-dark: #17484f;
    --band-text: #0a1619;
    --box-bg: #2b2d2e;
    --box-text: #f2f2f2;
  }
  * { margin: 0; padding: 0; box-sizing: border-box; }
  html, body {
    width: 927px;
    height: 1200px;
    overflow: hidden;
    background: var(--page-bg);
  }
  .canvas {
    position: relative;
    width: 927px;
    height: 1200px;
    background: var(--page-bg);
  }
  .label {
    position: absolute;
    left: 143px;
    top: 230px;
    width: 640px;
    height: 740px;
    background: var(--label-black);
    overflow: hidden;
    font-family: "Open Sans", sans-serif;
  }
  .label__halo {
    position: absolute;
    left: 70px;
    top: -150px;
    width: 500px;
    height: 500px;
    border-radius: 50%;
    background: radial-gradient(circle at 45% 45%, var(--circle-dark) 60%, #12272a 85%, var(--circle-edge) 100%);
  }
  .brand {
    position: absolute;
    left: 0;
    right: 0;
    top: 70px;
    display: flex;
    flex-direction: column;
    align-items: center;
    gap: 26px;
  }
  .brand__dot {
    width: 90px;
    height: 90px;
    border-radius: 50%;
    background: var(--brand-blue);
  }
  .brand__name {
    color: var(--brand-blue);
    font-weight: 400;
    font-size: 40px;
    letter-spacing: 1px;
    white-space: nowrap;
  }
  .claims {
    position: absolute;
    left: 0;
    right: 0;
    top: 418px;
    text-align: center;
    color: var(--teal-text);
    font-size: 25px;
    letter-spacing: 2px;
  }
  .function-band {
    position: absolute;
    left: 0;
    right: 0;
    top: 475px;
    height: 72px;
    background: linear-gradient(90deg, var(--band-dark) 0%, var(--band-light) 50%, var(--band-dark) 100%);
    display: flex;
    align-items: center;
    justify-content: center;
  }
  .function-band__title {
    color: var(--band-text);
    font-weight: 600;
    font-size: 31px;
    letter-spacing: 6px;
  }
  .function-band__shadow {
    position: absolute;
    left: 0;
    right: 0;
    top: 547px;
    height: 45px;
    background: linear-gradient(180deg, #123a40 0%, var(--label-black) 100%);
  }
  .dose-box {
    position: absolute;
    left: 50%;
    top: 620px;
    transform: translateX(-50%);
    padding: 16px 32px;
    background: var(--box-bg);
    color: var(--box-text);
    font-family: "Roboto Condensed", sans-serif;
    font-weight: 700;
    font-size: 30px;
    letter-spacing: 1px;
    white-space: nowrap;
  }
</style>
</head>
<body>
  <main class="canvas">
    <section class="label">
      <div class="label__halo"></div>
      <header class="brand">
        <span class="brand__dot"></span>
        <span class="brand__name">Verdant Halcyon Labs</span>
      </header>
      <p class="claims">100% ORGANIC &nbsp;|&nbsp; 100% PURE</p>
      <div class="function-band">
        <h1 class="function-band__title">ANXIETY RELIEF</h1>
      </div>
      <div class="function-band__shadow"></div>
      <p class="dose-box">750mg | 30 capsules</p>
    </section>
  </main>
</body>
</html>
```